International Travel Agency Needs 5 Banners for stands at Wedding Fayres

We need 5 banners to showcase our company at Wedding fairs. Each one would showcase luxury honeymoons on a different continent out of Europe, South East Asia, North America, Central America and Africa. They would need to include a small version of our logo attached but otherwise up to discretion of designer. Could include beautiful appealing pictures to entice brides and grooms with some complimentary alluring text about the destinations showcased in the pictures. All pictures and text must be provided at the discretion of the designer freely available for us to use without copyright infringement.

Banners design should be possible for 200mm by 80mm prints in high resolution

Target Market(s)

Brides and grooms

Colors

Designer to choose colors to be used in the design.

Requirements
Must have
• High resolution
No copyright infringement

```html
<!DOCTYPE html>
<html lang="en">
<head>
<meta charset="UTF-8">
<title>Africa – Honeymoon Banner</title>
<link href="https://fonts.googleapis.com/css2?family=Questrial&family=Open+Sans:wght@600&display=swap" rel="stylesheet">
<style>
  :root {
    --page: #ffffff;
    --leaf: #9bc953;
    --text-light: #ffffff;
    --rule: rgba(255, 255, 255, 0.85);
    --sky-top: #c9d2da;
    --sky-low: #e6eaee;
    --horizon: #8a9a6a;
    --savanna: #6f8a3c;
    --savanna-deep: #4f6a2a;
    --badge: rgba(255, 255, 255, 0.72);
    --brand-ink: #3f6a2c;
  }
  html, body {
    margin: 0;
    padding: 0;
    width: 1200px;
    height: 540px;
    overflow: hidden;
    background: var(--page);
  }
  .canvas {
    position: relative;
    width: 1200px;
    height: 540px;
    background: var(--page);
  }
  .banner {
    position: absolute;
    left: 67px;
    top: 56px;
    width: 1064px;
    height: 426px;
    display: flex;
  }
  .intro-panel {
    width: 362px;
    height: 100%;
    background: var(--leaf);
    color: var(--text-light);
    box-sizing: border-box;
    padding-top: 52px;
    text-align: center;
  }
  .destination-title {
    margin: 0;
    font-family: "Questrial", sans-serif;
    font-weight: 400;
    font-size: 76px;
    line-height: 1;
    letter-spacing: 1px;
  }
  .title-rule {
    width: 311px;
    height: 0;
    border: 0;
    border-top: 2px solid var(--rule);
    margin: 22px auto 26px;
  }
  .destination-pitch {
    margin: 0 auto;
    width: 280px;
    font-family: "Open Sans", sans-serif;
    font-weight: 600;
    font-size: 22.5px;
    line-height: 36.5px;
  }
  .scene-photo {
    position: relative;
    flex: 1;
    height: 100%;
    background: linear-gradient(
      to bottom,
      var(--sky-top) 0%,
      var(--sky-low) 45%,
      var(--horizon) 52%,
      var(--savanna) 68%,
      var(--savanna-deep) 100%
    );
  }
  .brand-badge {
    position: absolute;
    left: 416px;
    top: 166px;
    width: 250px;
    height: 250px;
    border-radius: 50%;
    background: var(--badge);
    display: flex;
    align-items: center;
    justify-content: center;
  }
  .brand-name {
    margin: 0;
    text-align: center;
    font-family: "Questrial", sans-serif;
    font-weight: 400;
    font-size: 32px;
    line-height: 1.15;
    color: var(--brand-ink);
  }
</style>
</head>
<body>
  <div class="canvas">
    <section class="banner">
      <div class="intro-panel">
        <h1 class="destination-title">Africa</h1>
        <hr class="title-rule">
        <p class="destination-pitch">If you are looking for something extraordinary &amp; are not worried about getting a bit dusty Africa is the destination for you.</p>
      </div>
      <div class="scene-photo" role="img" aria-label="A couple seen from behind leaning on a wooden rail, looking out over green African savanna under a cloudy sky">
        <div class="brand-badge">
          <p class="brand-name">Marigold Lane<br>Holidays</p>
        </div>
      </div>
    </section>
  </div>
</body>
</html>
```